Plorvantix Redesign Website

Looking for a web design who can think out of the box.
Redesign of www.plorvantix.com.au.
Design requirements:
- Use of many different Colors based on icon logo
- Use of nature and animal pictures that symbolize evolution, transition, metamorphosis, change, etc.
- Website background color for each page is based on Icon logo
- Website mood: Transition & Change, Water, Natural cycle, Waves, Natural evolution, Circle, Wheel,
- Landing page design with animated grafik based on logo icon
- Define colorful design flow that incorporates the website content (see attached file)
- Website development in Wix, access will be provided after final design

Target Market(s)

Non-for-profits in Health and Social sector, local small businesses

Industry/Entity Type

Community Development, Health, Aged-Care,

Coding

Coded - Design and coding required

Number of Pages Required

5+ page

Font styles to use
Sans Serif
Other font styles liked:
• MavenPro, Futura,

Colors
00AB8E
00BBA5
67D7C9
C6EFE9
E9F9F6
FFC000
F8CF3A
FAE287
FDF2CF
FEFAEE
F0912C
F2A743
F7CA91
FBE8D2
FDF5EE

Requirements
Must have
• Landing page with animated grafik, responsive design, out-of-box design, all pages and functions on current website, animated text and design ellements on all sides,
Nice to have
• use logo icon for landing page; it would be great if icon could be animated for the landing page, e.g. moving circles that coming out ot the head
Should not have
• look like a wix template, center aligments in block desciptions, corporate look

```html
<!DOCTYPE html>
<html lang="en">
<head>
<meta charset="utf-8">
<title>Plorvantix</title>
<link rel="stylesheet" href="https://fonts.googleapis.com/css2?family=Maven+Pro:wght@400;500;700&family=Roboto+Condensed:wght@400&display=swap">
<style>
:root{
  --teal:#00AB8E;
  --teal-mid:#00BBA5;
  --teal-soft:#67D7C9;
  --teal-pale:#C6EFE9;
  --teal-mist:#E9F9F6;
  --yellow:#FFC000;
  --yellow-soft:#FAE287;
  --orange:#F0912C;
  --orange-soft:#F7CA91;
  --ink:#1e1e1e;
  --text:#3a3a3a;
  --field:#e4efed;
  --teal-dark:#008a73;
  --footer:#1f2a28;
}
*{margin:0;padding:0;box-sizing:border-box}
html,body{width:1200px;height:3254px;overflow:hidden}
body{position:relative;background:#fff;font-family:'Maven Pro',sans-serif;color:var(--text)}
.abs{position:absolute}
.btn{position:absolute;background:var(--orange);color:#fff;border-radius:8px;font:500 16px 'Maven Pro',sans-serif;display:flex;align-items:center;justify-content:center;box-shadow:4px 4px 8px rgba(0,0,0,.16)}
.rule{position:absolute;height:3px;background:var(--orange)}
.ghost-label{position:absolute;font:400 64px 'Maven Pro',sans-serif;color:var(--teal-pale);writing-mode:vertical-rl;letter-spacing:2px;line-height:1}

/* hero */
.hero{position:absolute;left:0;top:0;width:1200px;height:646px;background:radial-gradient(ellipse at 30% 40%,#ffffff 0%,var(--teal-mist) 45%,#bfd9d4 100%)}
.hero-art{position:absolute;right:0;top:110px;width:610px;height:536px;background:radial-gradient(ellipse at 55% 45%,rgba(0,171,142,.35),rgba(240,145,44,.15) 55%,transparent 75%)}
.brand{position:absolute;left:100px;top:14px;width:96px;display:flex;flex-direction:column;align-items:center;gap:4px;font:700 17px 'Maven Pro',sans-serif;color:var(--ink)}
.brand .dot{width:44px;height:44px;border-radius:50%;background:var(--yellow)}
.nav a{position:absolute;top:38px;font:400 22px 'Maven Pro',sans-serif;color:var(--ink);text-decoration:none}
.login{position:absolute;left:972px;top:33px;width:104px;height:35px;border-radius:18px;background:var(--teal);color:#fff;font:500 16px 'Maven Pro',sans-serif;display:flex;align-items:center;gap:10px;padding-left:4px}
.login .avatar{width:28px;height:28px;border-radius:50%;background:#fff}
.hero h1{position:absolute;left:100px;top:166px;font:400 53px/1.1 'Maven Pro',sans-serif;color:var(--ink)}
.hero h1 strong{display:block;color:var(--teal);font-weight:700;margin-top:2px}
.quote{position:absolute;left:100px;top:304px;font:400 19px/30px 'Maven Pro',sans-serif;color:var(--ink)}
.author{position:absolute;left:168px;top:413px;font:500 25px 'Maven Pro',sans-serif;color:var(--ink)}

/* about */
.about-shadow{position:absolute;left:101px;top:724px;width:397px;height:356px;background:var(--teal)}
.about-photo{position:absolute;left:83px;top:701px;width:397px;height:356px;background:linear-gradient(160deg,#dfe7ea 0%,#7fa7b0 35%,#2e7f8c 65%,#1b5e6a 100%)}
.about h2{position:absolute;left:575px;top:742px;font:700 25px 'Maven Pro',sans-serif;color:var(--ink)}
.about .sub{position:absolute;left:575px;top:788px;font:400 19px 'Roboto Condensed',sans-serif;color:var(--teal)}
.about p{position:absolute;left:575px;top:834px;width:524px;font:400 16.5px/26px 'Roboto Condensed',sans-serif;text-align:justify;color:var(--text)}

/* video */
.video{position:absolute;left:0;top:1168px;width:1200px;height:550px;background:var(--teal-mist)}
.video-title{position:absolute;left:96px;top:1203px;font:700 30px 'Maven Pro',sans-serif;color:var(--ink)}
.video-panel{position:absolute;left:0;top:1267px;width:688px;height:451px;background:var(--teal);color:#fff}
.video-panel h3{position:absolute;left:101px;top:47px;font:700 25px 'Maven Pro',sans-serif}
.video-panel h4{position:absolute;left:101px;top:106px;width:500px;font:400 28px/39px 'Maven Pro',sans-serif}
.video-panel p{position:absolute;left:100px;top:252px;width:503px;font:400 15px/26px 'Maven Pro',sans-serif;text-align:justify}
.video-main{position:absolute;left:623px;top:1212px;width:478px;height:300px;background:linear-gradient(180deg,#aec6dc 0%,#e8eef2 55%,#f4f6f6 72%,#7fb04a 100%)}
.play{position:absolute;left:828px;top:1323px;width:56px;height:56px}
.thumb{position:absolute;top:1526px;width:152px;height:116px}

/* contact */
.gt-title{position:absolute;left:98px;top:1846px;font:700 27px 'Maven Pro',sans-serif;color:var(--ink)}
.gt-title span,.ct-title span{color:var(--teal)}
.field{position:absolute;left:98px;width:515px;height:43px;background:var(--field);border-radius:6px;font:400 15px 'Maven Pro',sans-serif;color:var(--ink);padding:12px 9px}
.ct-title{position:absolute;left:706px;top:1841px;font:700 27px 'Maven Pro',sans-serif;color:var(--ink)}
.ct-text{position:absolute;left:711px;top:1893px;width:390px;font:400 15.5px/34px 'Maven Pro',sans-serif;color:var(--ink)}
.ct-line{position:absolute;left:770px;font:400 22px 'Maven Pro',sans-serif;color:var(--ink)}

/* testimonial */
.testi{position:absolute;left:0;top:2358px;width:1200px;height:490px;background:var(--teal-mid)}
.testi-block{position:absolute;left:75px;top:49px;width:162px;height:167px;border-radius:14px;background:var(--teal-dark)}
.testi-photo{position:absolute;left:98px;top:68px;width:355px;height:379px;border-radius:14px;background:linear-gradient(180deg,#4aa7e0 0%,#7fc4ea 45%,#a9b36a 75%,#6a8a3a 100%)}
.testi .line{position:absolute;left:480px;width:606px;height:1px;background:var(--orange-soft)}
.testi h2{position:absolute;left:483px;top:92px;font:700 31px 'Maven Pro',sans-serif;color:#fff}
.testi p{position:absolute;left:488px;top:166px;width:600px;font:400 17.5px/23px 'Maven Pro',sans-serif;color:#fff}
.testi .who{position:absolute;left:493px;top:298px;font:500 21px 'Maven Pro',sans-serif;color:#fff}
.dots{position:absolute;left:499px;top:369px;display:flex;gap:6px}
.dots i{width:9px;height:9px;border-radius:50%;background:#fff}
.dots i:first-child{background:var(--yellow)}
.role{position:absolute;right:114px;top:361px;font:500 23px 'Maven Pro',sans-serif;color:var(--yellow-soft)}

/* footer */
.footer{position:absolute;left:0;top:2848px;width:1200px;height:406px;background:linear-gradient(180deg,#24302e 0%,var(--footer) 60%,#18201e 100%);color:#fff}
.f-brand{position:absolute;left:0;width:1200px;top:46px;text-align:center;font:700 22px 'Maven Pro',sans-serif}
.f-brand .dot{display:block;margin:0 auto 10px;width:54px;height:54px;border-radius:50%;background:var(--yellow)}
.f-brand .under{display:block;margin:8px auto 0;width:44px;height:2px;background:#fff}
.f-nav a{position:absolute;top:193px;font:400 23px 'Maven Pro',sans-serif;color:#fff;text-decoration:none}
.social{position:absolute;top:261px;width:30px;height:30px;border-radius:50%;border:2px solid var(--teal-soft)}
.copy{position:absolute;left:0;width:1200px;top:328px;text-align:center;font:400 17px 'Maven Pro',sans-serif}
</style>
</head>
<body>

<section class="hero">
  <div class="hero-art" role="img" aria-label="Human profile dissolving into leaves beside a bare tree under cloudy sky"></div>
  <div class="brand"><span class="dot"></span>Plorvantix</div>
  <nav class="nav">
    <a style="left:244px">Home</a>
    <a style="left:350px">About</a>
    <a style="left:455px">Services</a>
    <a style="left:585px">Contact</a>
  </nav>
  <div class="login"><span class="avatar"></span>LOGIN</div>
  <h1>WELCOME TO<strong>PLORVANTIX</strong></h1>
  <div class="quote">“Yesterday I was clever, so<br>I wanted to change the world.<br>Today I am wise, so I am changing myself.”</div>
  <div class="rule" style="left:100px;top:428px;width:50px;height:2px"></div>
  <div class="author">Arvel Domsky</div>
</section>

<section class="about">
  <div class="about-shadow"></div>
  <div class="about-photo" role="img" aria-label="Turquoise ocean wave breaking with white spray"></div>
  <div class="rule" style="left:575px;top:723px;width:110px"></div>
  <h2>OUR LEARNINGS OVER THE YEARS</h2>
  <div class="sub">Technology Alone Won’t Help You</div>
  <p>Fortunately or unfortunately, the shiny technology isn’t a silver bullet you have been searching for. New technology can get you only so far. The challenge here is transforming the mindsets, behaviours with the new ways of working. Hence, the combination of these two will lead to true organisational transformation. Improved performance is a combination of being effective, efficient, and technology.</p>
  <div class="btn" style="left:576px;top:1026px;width:135px;height:43px">READ MORE</div>
  <div class="ghost-label" style="left:1128px;top:697px">ABOUT US</div>
</section>

<section class="video"></section>
<div class="rule" style="left:0;top:1220px;width:80px"></div>
<h2 class="video-title">OUR VIDEO</h2>
<div class="video-panel">
  <h3>NON-BIOS SYSTEM REVIEW</h3>
  <h4>ARE YOU LOOKING INTO A CLIENT MANAGEMENT SYSTEM AND DON’T KNOW WHERE TO BEGIN?</h4>
  <p>Our team does requirement workshops with your key staff members. Based on the requirements, we do a tool based agnostic research which is the best-fit solution for you, minus provider bios.</p>
  <div class="btn" style="left:100px;top:354px;width:135px;height:44px">READ MORE</div>
</div>
<div class="video-main" role="img" aria-label="Video still: a tree half bare in snow and half green in summer"></div>
<svg class="play" viewBox="0 0 56 56" aria-hidden="true"><circle cx="28" cy="28" r="28" fill="#F0912C"/><path d="M22 17 L40 28 L22 39 Z" fill="#fff"/></svg>
<div class="thumb" style="left:623px;background:linear-gradient(160deg,#cfe39a,#3f7a2a 60%,#1d3a15)" role="img" aria-label="Seedlings sprouting in sunlight"></div>
<div class="thumb" style="left:787px;background:linear-gradient(180deg,#a9c08f,#6e8c5a 55%,#5a5a55)" role="img" aria-label="Young green plant growing from soil"></div>
<div class="thumb" style="left:948px;background:linear-gradient(180deg,#a8c6e6,#c9d3c6 50%,#8a8a3e 80%,#b84030)" role="img" aria-label="Cyclist riding through a flower meadow"></div>
<div class="ghost-label" style="left:1136px;top:1276px">OUR VIDEO</div>

<section class="contact">
  <div class="rule" style="left:0;top:1861px;width:80px"></div>
  <h2 class="gt-title"><span>GET IN</span> TOUCH</h2>
  <div class="field" style="top:1911px">Name</div>
  <div class="field" style="top:1973px">Email Address</div>
  <div class="field" style="top:2032px">Phone Number</div>
  <div class="field" style="top:2092px;height:104px;padding:13px 12px">Message</div>
  <div class="btn" style="left:102px;top:2210px;width:125px;height:47px;border-radius:24px;font-weight:700;font-size:15px">SUBMIT</div>

  <h2 class="ct-title"><span>CONTACT</span> US</h2>
  <div class="ct-text">Faced with a project that requires change management? Simply fill out the form and our team will get back to you shortly. Not a fan of forms?</div>
  <svg class="abs" style="left:714px;top:2016px" width="38" height="38" viewBox="0 0 38 38" aria-hidden="true"><circle cx="19" cy="19" r="17.5" fill="none" stroke="#00AB8E" stroke-width="1.6"/><path d="M13 11c1-1 2-1 3 0l2 3c.5 1 0 2-1 2.5 1 2.5 2.5 4 5 5 .5-1 1.5-1.5 2.5-1l3 2c1 1 1 2 0 3-2 2-5 2-9-2s-7-8-5.5-12.5z" fill="none" stroke="#222" stroke-width="1.5"/></svg>
  <div class="ct-line" style="top:2022px">+614-000-55217</div>
  <svg class="abs" style="left:714px;top:2085px" width="38" height="38" viewBox="0 0 38 38" aria-hidden="true"><circle cx="19" cy="19" r="17.5" fill="none" stroke="#00AB8E" stroke-width="1.6"/><rect x="11" y="13" width="16" height="12" rx="1.5" fill="none" stroke="#222" stroke-width="1.5"/><path d="M11 14l8 6 8-6" fill="none" stroke="#222" stroke-width="1.5"/></svg>
  <div class="ct-line" style="top:2091px">getintouch@plorvantix.com</div>
</section>

<section class="testi">
  <div class="testi-block"></div>
  <div class="testi-photo" role="img" aria-label="Woman in a blue helmet riding a bicycle through a meadow"></div>
  <div class="line" style="top:77px"></div>
  <h2>What do Our Clients Have to Say</h2>
  <p>"We are thrilled by the enthusiasm and passion of the Plorvantix group. Their team is highly experienced, human-centred and understand the problems organisations go through while transforming. They truly helped us achieve our objectives."</p>
  <div class="who">-Marisa T.</div>
  <div class="line" style="top:357px"></div>
  <div class="dots"><i></i><i></i><i></i><i></i></div>
  <div class="role">Operations Manager &#x27F6;</div>
</section>

<footer class="footer">
  <div class="f-brand"><span class="dot"></span>Plorvantix<span class="under"></span></div>
  <nav class="f-nav">
    <a style="left:390px">Home</a>
    <a style="left:495px">About</a>
    <a style="left:601px">Services</a>
    <a style="left:731px">Contact</a>
  </nav>
  <span class="social" style="left:510px"></span>
  <span class="social" style="left:558px"></span>
  <span class="social" style="left:606px"></span>
  <span class="social" style="left:656px"></span>
  <div class="copy">© copyrights 2022 © plorvantix&nbsp; All Rights Reserved</div>
</footer>

</body>
</html>
```